Head, Heart , Hands

A bright, eye-catching poster depicting the theme " Head, Heart, Hands".

The school logo attached needs to be small and in the bottom right-hand corner.

```html
<!DOCTYPE html>
<html lang="en">
<head>
<meta charset="utf-8">
<title>Head. Heart. Hands. — Poster</title>
<link rel="stylesheet" href="https://fonts.googleapis.com/css2?family=Barlow+Condensed:wght@400;600&display=swap">
<style>
  :root {
    --sun-yellow: #f3e84c;
    --olive: #c2b400;
    --charcoal: #3a3a3c;
    --badge-blue: #9cc3e6;
  }
  html, body {
    margin: 0;
    padding: 0;
    overflow: hidden;
    background: var(--sun-yellow);
  }
  .poster {
    position: relative;
    width: 800px;
    height: 1200px;
    overflow: hidden;
    background: var(--sun-yellow);
    font-family: "Barlow Condensed", "Arial Narrow", sans-serif;
    color: var(--charcoal);
  }
  .poster__frame {
    position: absolute;
    left: 78px;
    top: 69px;
    width: 644px;
    height: 1061px;
    border: 3px solid var(--charcoal);
    box-sizing: border-box;
  }
  .poster__shapes {
    position: absolute;
    inset: 0;
    width: 800px;
    height: 1200px;
  }
  .shape { fill: var(--olive); }
  .poster__title {
    position: absolute;
    left: 156px;
    top: 342px;
    margin: 0;
    font-size: 156px;
    line-height: 134px;
    font-weight: 400;
    letter-spacing: -1px;
  }
  .poster__title span { display: block; }
  .poster__title .title-heart { font-weight: 600; }
  .school-mark {
    position: absolute;
    right: 98px;
    bottom: 110px;
    display: flex;
    align-items: center;
    gap: 8px;
  }
  .school-mark__dot {
    width: 26px;
    height: 26px;
    border-radius: 50%;
    background: var(--badge-blue);
  }
  .school-mark__name {
    font-size: 20px;
    font-weight: 600;
    color: var(--charcoal);
    letter-spacing: 0.5px;
  }
</style>
</head>
<body>
  <main class="poster">
    <svg class="poster__shapes" viewBox="0 0 800 1200" xmlns="http://www.w3.org/2000/svg">
      <path class="shape hand-area" role="img" aria-label="Silhouette of an open hand reaching down from the top-left corner"
            d="M0,0 L150,0 C200,40 250,110 272,190 C282,235 260,268 220,262 C160,250 80,200 30,140 C10,110 0,80 0,60 Z"/>
      <path class="shape heart" d="M743,745 L584,586 A112.4,112.4 0 0 1 743,427 A112.4,112.4 0 0 1 902,586 Z"/>
      <path class="shape head-area" role="img" aria-label="Silhouette of a human head in profile rising from the bottom-left corner"
            d="M0,885 C50,855 150,845 210,880 C255,910 270,970 268,1030 C266,1090 250,1140 250,1200 L0,1200 Z"/>
    </svg>

    <div class="poster__frame"></div>

    <h1 class="poster__title">
      <span class="title-head">Head.</span>
      <span class="title-heart">Heart.</span>
      <span class="title-hands">Hands.</span>
    </h1>

    <div class="school-mark">
      <span class="school-mark__dot"></span>
      <span class="school-mark__name">St Brigid's Hillcrest</span>
    </div>
  </main>
</body>
</html>
```